Music Festival Business Cards

The Lanternmoor Festival
Produced by Bramblewick Sound Group LLC
New music festival in Arkansas.

Target Market(s)

18-35 year olds

Industry/Entity Type

Festival

Contact Information for Business Card

We are a 5-partner team producing a music festival in Arkansas. We need slick business cards, and I want them to be square.

Requirements
Must have
• I NEED THESE TO BE IN SQUARE SIZE - 2x2 or 2.5x2.5... please not regular size.
• I need www.thelanternmoor.live as the link to website.

```html
<!DOCTYPE html>
<html lang="en">
<head>
<meta charset="utf-8">
<title>The Lanternmoor Festival – Business Cards</title>
<link rel="stylesheet" href="https://fonts.googleapis.com/css2?family=Orbitron:wght@500;600&family=Roboto:wght@400&display=swap">
<style>
  :root {
    --page-bg: #e6e2dc;
    --card-bg: #121212;
    --card-bg-edge: #1b1b1b;
    --accent: #45c1cc;
    --ink: #ffffff;
    --rule: #d8d8d8;
  }
  html, body {
    margin: 0;
    padding: 0;
    width: 900px;
    height: 1200px;
    overflow: hidden;
    background: var(--page-bg);
  }
  .canvas {
    position: relative;
    width: 900px;
    height: 1200px;
  }
  .card {
    position: absolute;
    left: 200px;
    width: 500px;
    height: 500px;
    background: linear-gradient(90deg, var(--card-bg) 0%, var(--card-bg-edge) 100%);
    box-shadow: 0 6px 18px rgba(0,0,0,0.35);
    overflow: hidden;
  }
  .card--front { top: 70px; }
  .card--back { top: 630px; }
  .card__band {
    position: absolute;
    left: 0; right: 0; bottom: 0;
    height: 15px;
    background: var(--accent);
  }
  .person__name {
    position: absolute;
    left: 40px; top: 52px;
    margin: 0;
    font: 600 26px/1 "Orbitron", sans-serif;
    letter-spacing: 2px;
    color: var(--ink);
  }
  .person__title {
    position: absolute;
    left: 40px; top: 88px;
    margin: 0;
    font: 500 12px/1 "Orbitron", sans-serif;
    letter-spacing: 3px;
    color: var(--accent);
  }
  .address {
    position: absolute;
    left: 40px; top: 124px;
    margin: 0;
    font: 400 17px/28px "Roboto", sans-serif;
    font-style: normal;
    color: var(--ink);
  }
  .front-wordmark {
    position: absolute;
    left: 40px; top: 232px;
    font: 600 20px/1 "Orbitron", sans-serif;
    letter-spacing: 1px;
    color: var(--accent);
  }
  .rule {
    position: absolute;
    top: 300px;
    height: 1px;
    background: var(--rule);
  }
  .rule--left { left: 40px; width: 300px; }
  .rule--right { left: 390px; width: 70px; }
  .contact {
    position: absolute;
    left: 40px; top: 318px;
    margin: 0; padding: 0;
    list-style: none;
  }
  .contact__item {
    display: flex;
    align-items: center;
    height: 32px;
    font: 400 17px/1 "Roboto", sans-serif;
    color: var(--ink);
  }
  .contact__icon {
    width: 18px; height: 16px;
    margin-right: 12px;
    fill: var(--accent);
  }
  .brand-mark {
    position: absolute;
    left: 226px; top: 120px;
    width: 48px; height: 48px;
    background: var(--accent);
  }
  .brand-name {
    position: absolute;
    left: 0; right: 0; top: 262px;
    margin: 0;
    text-align: center;
    font: 600 30px/1 "Orbitron", sans-serif;
    letter-spacing: 1px;
    color: var(--accent);
  }
  .brand-producer {
    position: absolute;
    left: 0; right: 0; top: 308px;
    margin: 0;
    text-align: center;
    font: 500 12px/1 "Orbitron", sans-serif;
    letter-spacing: 0.5px;
    color: var(--accent);
  }
  .brand-web {
    position: absolute;
    left: 0; right: 0; top: 404px;
    margin: 0;
    text-align: center;
    font: 400 16px/1 "Roboto", sans-serif;
    color: var(--ink);
  }
</style>
</head>
<body>
<main class="canvas">
  <section class="card card--front" aria-label="Card front">
    <h1 class="person__name">MARCUS HALE</h1>
    <p class="person__title">MANAGING DIRECTOR</p>
    <address class="address">214 Cedar Ridge Road<br>Suite 308. Eureka AR 72631</address>
    <div class="front-wordmark">THE LANTERNMOOR</div>
    <div class="rule rule--left"></div>
    <div class="rule rule--right"></div>
    <ul class="contact">
      <li class="contact__item">
        <svg class="contact__icon" viewBox="0 0 18 16" aria-hidden="true"><path d="M1 5c0-2 3-3 8-3s8 1 8 3v1h-4V4.5c-1-.5-2.5-.7-4-.7s-3 .2-4 .7V6H1z"/><path d="M4 7h10l2 8H2z"/><circle cx="9" cy="11" r="2" fill="#121212"/></svg>
        27 10 555 0148
      </li>
      <li class="contact__item">
        <svg class="contact__icon" viewBox="0 0 18 16" aria-hidden="true"><rect x="4" y="1" width="10" height="4"/><rect x="1" y="6" width="16" height="6" rx="1"/><rect x="4" y="10" width="10" height="5"/><rect x="5.5" y="11.5" width="7" height="1" fill="#121212"/></svg>
        27 10 555 0148
      </li>
      <li class="contact__item">
        <svg class="contact__icon" viewBox="0 0 18 16" aria-hidden="true"><rect x="1" y="2" width="16" height="12"/><path d="M1.5 2.5 9 9l7.5-6.5" fill="none" stroke="#121212" stroke-width="1.4"/></svg>
        marcus@thelanternmoor.live
      </li>
      <li class="contact__item">
        <svg class="contact__icon" viewBox="0 0 18 16" aria-hidden="true"><circle cx="9" cy="8" r="7"/><path d="M2 8h14M9 1c-3 3.5-3 10.5 0 14M9 1c3 3.5 3 10.5 0 14" fill="none" stroke="#121212" stroke-width="1.2"/></svg>
        www.thelanternmoor.live
      </li>
    </ul>
    <div class="card__band"></div>
  </section>

  <section class="card card--back" aria-label="Card back">
    <div class="brand-mark" aria-hidden="true"></div>
    <h2 class="brand-name">THE LANTERNMOOR</h2>
    <p class="brand-producer">PRODUCED BY BRAMBLEWICK SOUND GROUP LLC</p>
    <p class="brand-web">www.thelanternmoor.live</p>
    <div class="card__band"></div>
  </section>
</main>
</body>
</html>
```